Redesign of Real Estate Agency Website

We need a redesign for our real estate agency website. Please see attached creative brief.

Target Market(s)

Refer to creative brief.

Industry/Entity Type

Real Estate

Requirements
Must have
• Refer to creative brief.

```html
<!DOCTYPE html>
<html lang="en">
<head>
<meta charset="utf-8">
<title>Palmreach – Phuket Property and Real Estate</title>
<link href="https://fonts.googleapis.com/css2?family=Arimo:wght@400;700&family=Tinos:wght@400;700&display=swap" rel="stylesheet">
<style>
:root{
  --red:#c0141c;
  --blue:#2a80b9;
  --text:#4a4a4a;
  --muted:#6a6a6a;
  --panel:#efefef;
  --panel-line:#d8d8d8;
  --teal-soft:#c9dfdb;
  --teal-dark:#4d7174;
  --teal-mid:#6f9497;
  --navy:#1d3e6e;
  --white:#fff;
}
*{box-sizing:border-box;margin:0;padding:0}
html,body{width:669px;height:1200px;overflow:hidden;background:var(--white)}
body{position:relative;font-family:"Arimo",Arial,sans-serif;color:var(--text);font-size:8px;line-height:1.35}
a{color:inherit;text-decoration:none}
ul{list-style:none}

.brand{position:absolute;left:22px;top:18px}
.brand-name{font-size:19px;font-weight:700;color:var(--navy);letter-spacing:-.3px;display:flex;align-items:center;gap:5px}
.brand-dot{width:7px;height:7px;border-radius:50%;background:var(--red)}
.brand-tag{font-size:6.5px;color:var(--muted);letter-spacing:.3px;margin-top:2px}

.carts{position:absolute;right:12px;top:18px;font-size:7px;color:var(--muted);display:flex;gap:6px;align-items:center}
.carts span b{font-weight:400;color:var(--blue)}

.hero{position:absolute;left:10px;top:58px;width:648px;height:297px;
  background:linear-gradient(180deg,#cfe1ea 0%,#e8e2d4 30%,#b88a68 48%,#6f7d4b 70%,#9b8464 100%)}

.search{position:absolute;left:422px;top:118px;width:214px;height:206px;background:rgba(255,255,255,.93);padding:14px 21px 0}
.search h2{font-size:7px;font-weight:700;color:#333;border-bottom:1px solid var(--blue);padding-bottom:6px;margin-bottom:7px}
.field label{display:block;font-size:7px;font-weight:700;color:#333;margin-bottom:2px}
.select{height:10px;border:1px solid #9a9a9a;background:var(--white);position:relative;margin-bottom:7px}
.select::after{content:"";position:absolute;right:0;top:0;width:9px;height:8px;background:#777}
.pair{display:flex;gap:10px}.pair .field{flex:1}
.search-foot{display:flex;justify-content:space-between;align-items:center;margin-top:4px}
.search-foot a{color:var(--blue);text-decoration:underline;font-size:7px}
.btn-find{background:#7c7c7c;color:var(--white);font-size:7px;font-weight:700;padding:1px 8px;border:1px solid #555}

.nav{position:absolute;left:10px;top:355px;width:648px;height:25px;background:var(--teal-soft);display:flex;align-items:center;padding-left:20px;font-size:7px;color:#555;letter-spacing:.3px}
.nav a{padding:0 12px}
.nav a.active{font-weight:700;color:#222;padding-left:0}
.nav i{font-style:normal;color:#888}

.col{position:absolute;top:397px;height:562px;background:var(--panel);border:1px solid var(--panel-line);padding:10px 8px}
.col-sale{left:10px;width:231px}
.col-rent{left:254px;width:233px}
.col h1{font-family:"Tinos",Georgia,serif;font-weight:400;font-size:15px;color:var(--red);margin-bottom:9px}
.photo{height:90px;margin:0 3px 14px}
.photo-sale{background:linear-gradient(180deg,#9ec3e4,#d9b08c 55%,#5e7e4c)}
.photo-rent{background:linear-gradient(180deg,#6d8fb4,#c7b9a0 50%,#4c4a44)}
.col h3{font-family:"Tinos",Georgia,serif;font-weight:700;font-size:9.5px;color:var(--blue);margin-bottom:9px}
.col h4{font-size:8.5px;font-weight:700;color:#555;margin-bottom:9px}
.links li{color:var(--red);margin-bottom:8px;font-size:8px}
.bullets li{position:relative;padding-left:11px;margin-bottom:10px;color:var(--muted);font-size:7.5px}
.bullets li::before{content:"";position:absolute;left:0;top:4px;width:4px;height:1px;background:#999}
.bullets li.red{color:var(--red)}
.bullets a{color:var(--red)}
.col-rent h4{margin-top:14px}

.widget{position:absolute;left:497px;width:161px;border:1px solid #b9cbc9;background:var(--white)}
.widget-head{height:16px;background:linear-gradient(180deg,var(--teal-mid),var(--teal-dark));color:var(--white);font-size:7px;font-weight:700;padding:4px 7px}
.w-map{top:398px;height:248px}
.radios{display:flex;justify-content:center;gap:12px;padding:5px 0;font-size:8px;color:#333}
.radio{display:inline-block;width:8px;height:8px;border:1px solid #666;border-radius:50%;vertical-align:-1px;margin-right:3px}
.radio.on{background:radial-gradient(circle,#2a9d4a 35%,var(--white) 45%)}
.map{margin:2px 10px;height:180px;background:linear-gradient(160deg,#e8f3fb,#cfe6f5)}
.map-link{text-align:center;color:var(--navy);text-decoration:underline;font-size:6.5px;margin-top:5px}
.w-news{top:658px;height:84px}
.w-news p{padding:9px 7px 6px;font-size:7px;color:var(--muted)}
.news-form{display:flex;gap:4px;padding:0 7px}
.news-input{width:102px;height:13px;background:#c4dcd6;font-size:7px;color:#555;padding:2px 6px}
.news-submit{background:var(--red);color:var(--white);font-size:7px;font-weight:700;padding:2px 5px}
.w-hello{top:754px;height:205px}
.w-hello p{padding:7px 7px 0;font-size:7px;color:var(--muted)}
.w-hello p.strong{color:var(--red);font-weight:700}
.team{position:absolute;left:0;bottom:0;width:100%;height:65px;background:linear-gradient(180deg,#f2f2f2,#b7a79a 60%,#3a3a3a)}

.footer{position:absolute;left:10px;top:978px;width:648px;height:172px;background:var(--teal-soft);display:flex;padding:7px 0 0 10px}
.f-col{width:167px;padding:0 0 0 0;border-right:1px solid #a9c3be;margin-right:20px;font-size:7.5px;color:#444;line-height:1.27}
.f-col:last-child{border-right:0}
.f-col h5{font-size:7.5px;font-weight:700;color:#333}
.f-col h5.gap{margin-top:6px}
.copy{position:absolute;top:1161px;left:0;width:669px;text-align:center;font-size:7.5px;color:#555}
</style>
</head>
<body>

<header>
  <div class="brand">
    <div class="brand-name">Palmreach <span class="brand-dot"></span></div>
    <div class="brand-tag">PHUKET PROPERTY AND REAL ESTATE</div>
  </div>
  <div class="carts">
    <svg width="18" height="14" viewBox="0 0 18 14" aria-hidden="true"><path d="M1 2h3l2 8h9l2-6H5" fill="none" stroke="#777" stroke-width="1.3"/><circle cx="7" cy="12" r="1.3" fill="#777"/><circle cx="14" cy="12" r="1.3" fill="#777"/></svg>
    <div>
      <span>0 items in <b>sales inquiry cart</b></span><br>
      <span>0 items in <b>rentals inquiry cart</b></span>
    </div>
  </div>
</header>

<div class="hero" role="img" aria-label="Photo of a large villa with a tiled roof and landscaped garden"></div>

<form class="search">
  <h2>QUICK PROPERTY SEARCH</h2>
  <div class="field"><label>Buy Property</label><div class="select"></div></div>
  <div class="field"><label>Property Type</label><div class="select"></div></div>
  <div class="pair">
    <div class="field"><label>Region</label><div class="select"></div></div>
    <div class="field"><label>District</label><div class="select"></div></div>
  </div>
  <div class="field"><label>Minimum Bedrooms</label><div class="select"></div></div>
  <div class="field"><label>Maximum Price (THB)</label><div class="select"></div></div>
  <div class="search-foot"><a href="#">Advanced search</a><span class="btn-find">Find Proposals</span></div>
</form>

<nav class="nav">
  <a class="active" href="#">HOME</a><i>|</i>
  <a href="#">PROPERTY FOR SALE</a><i>|</i>
  <a href="#">PROPERTY FOR RENT</a><i>|</i>
  <a href="#">CONTACT US</a><i>|</i>
  <a href="#">ABOUT US</a><i>|</i>
  <a href="#">LIST YOUR PROPERTY</a><i>|</i>
  <a href="#">PROPERTY BUYER'S GUIDE</a>
</nav>

<section class="col col-sale">
  <h1>PROPERTY FOR SALE</h1>
  <div class="photo photo-sale" role="img" aria-label="Photo of a villa for sale"></div>
  <h3>THE SERVICES WE OFFER</h3>
  <h4>Comprehensive service with integrity:</h4>
  <ul class="links">
    <li>Hot properties for sale</li>
    <li>Search properties for sale in Phuket</li>
    <li>Search properties for rent in Phuket</li>
    <li>Hot deals on holiday rentals</li>
    <li>Contact us</li>
    <li>About us</li>
  </ul>
  <ul class="bullets">
    <li>Extensive selection of Phuket properties for sale and rent.</li>
    <li>Research and suggest properties that meet our clients' requirements.</li>
    <li>Arrange property sales and rentals viewings.</li>
    <li>Chauffer and escort clients throughout their property viewings.</li>
    <li>Provide independent advice regarding buying and renting property in Phuket.</li>
    <li>Offer unbiased legal information and can assist in appointing independent lawyers.</li>
    <li>Provide the best possible deal for our clients by negotiating with sellers and developers.</li>
    <li>Provide a comprehensive after-sales service by liaising with all parties involved.</li>
    <li>Provide regular updates to clients on their property purchase.</li>
    <li>Provide advice and support on all aspects of living in Phuket and Thailand.</li>
  </ul>
</section>

<section class="col col-rent">
  <h1>PROPERTY FOR RENT</h1>
  <div class="photo photo-rent" role="img" aria-label="Photo of a modern rental house at dusk"></div>
  <h3>WHY USE PALMREACH REAL ESTATE?</h3>
  <h4>Experience:</h4>
  <ul class="bullets">
    <li>Palmreach Real Estate is one of the most experienced independent Real Estate agents focusing completely on Phuket.</li>
    <li>Our team has lived on Phuket for a total of over 90 years and our experience with Real Estate exceeds 30 years, so we feel we are very well qualified to provide high quality services to our clients. <a href="#">About us</a></li>
    <li>Proven track record with many satisfied clients.</li>
  </ul>
  <h4>Choice:</h4>
  <ul class="bullets">
    <li>We have a wide selection of properties for sale and rent, including new developments, private homes, exclusive luxury homes and budget properties.</li>
    <li>We actively liaise with developers and sellers to ensure that our clients get the best deals and latest information.</li>
    <li class="red">Search our properties for sale</li>
  </ul>
  <h4>Independent and unbiased:</h4>
  <ul class="bullets">
    <li>As independent real estate agents we are able to offer entirely unbiased advice. We are not tied to specific developers or sellers so you will find us impartial in our advice and opinions.</li>
    <li>Our Services are free for property buyers and renters. We earn our income only from commission fees paid by the property sellers.</li>
  </ul>
</section>

<aside class="widget w-map">
  <div class="widget-head">Search by Map</div>
  <div class="radios"><span><i class="radio on"></i>Buy</span><span><i class="radio"></i>Rent</span></div>
  <div class="map" role="img" aria-label="Map of Phuket divided into North, East, West, Phuket Town &amp; Central and South regions"></div>
  <div class="map-link">View large map</div>
</aside>

<aside class="widget w-news">
  <div class="widget-head">Get Our Newsletter</div>
  <p>Get the latest Phuket Real Estate news and deals every month</p>
  <div class="news-form"><span class="news-input">Your Email Here</span><span class="news-submit">SUBMIT</span></div>
</aside>

<aside class="widget w-hello">
  <div class="widget-head">We look forward to hearing from you!</div>
  <p>Please look around our website to view our extensive property listings, or please feel free to contact us if you have any specific requirements and we will make suggestions based on your criteria.</p>
  <p>We will do our utmost to ensure that your experience in buying or renting real estate in Phuket is rewarding and pleasurable.</p>
  <p class="strong">We at Palmreach Real Estate look forward to finding the ideal Phuket property for you!</p>
  <div class="team" role="img" aria-label="Photo of the agency team"></div>
</aside>

<footer class="footer">
  <div class="f-col">
    <h5>phuket real estate for sale</h5>
    phuket property for sale index<br>search property for sale in phuket<br>apartments &amp; condos for sale in phuket<br>villas &amp; houses for sale in phuket<br>land for sale in phuket<br>commercial property for sale in phuket<br>luxury property for sale<br>property for sale map<br>property buyer's guide for phuket<br>why phuket?<br>property ownership rights<br>property taxes &amp; fees<br>land titles<br>land units<br>property faq
  </div>
  <div class="f-col">
    <h5>phuket property for rent</h5>
    phuket property for rent index<br>search property for rent in phuket<br>phuket holiday rentals<br>holiday villas<br>luxury villas<br>cheap villas<br>holiday apartments<br>holiday rentals booking guide<br>holiday rentals faq<br>terms &amp; conditions<br>samui holiday rentals<br>phuket long-term rentals<br>long-term villas &amp; houses<br>long-term apartments<br>property for rent map
  </div>
  <div class="f-col">
    <h5>site links</h5>
    palmreach real estate index<br>privacy policy<br>disclaimer<br>site map
    <h5 class="gap">about palmreach real estate</h5>
    about us<br>contact us<br>list your property<br>selling your property
  </div>
  <div class="f-col">
    <h5>phuket info</h5>
    palmreach homepage<br>travel info<br>tours<br>dining &amp; nightlife<br>expats<br>directory<br>classified ads<br>hotels
  </div>
</footer>

<div class="copy">Phuket Real Estate from Palmreach | Copyright © Palmreach 2008. All Rights Reserved</div>

</body>
</html>
```